Exciting Poster Project: 4 posters for Employee Benefit Program

We are an entrepreneurial healthcare IT company that is creating an internal campaign to launch our 2017 Culture and Professional Development goals for our internal staff.

We need 4 posters utilizing the 4 campaign logos (attached) that are tied together visually into a cohesive campaign.

A PPT is included that shows the other wall art that currently exists on the walls. The new posters will share a space with these pieces.

The posters may be mounted side by side, or stand alone on a wall- so the design should work both ways. Each poster should include its own icon and the tag line provided along with topics provided that fall under this category. The posters size can be dictated by your design, but the text should be legible from a minimum of 8 feet away.

At the bottom of each poster should include all 4 icons in order to tie the entire campaign together (perhaps they can be arranged together like a diamond shape with the primary one as the biggest diamond)

Our company website for our external branding is: www.pelmaroq.com
We have included our branding guidelines for our external brand, and ppts and graphics for our internal brand.

1) Poster 1:
a. Header: Better Today Than Yesterday
b. Sub-title: Personal and Professional Growth
c. Description: We are committed to helping you build on your strengths and passions and support you your career advancement goals. We have a variety of training and development programs available to help you reach your top potential!
Leadership Development Programs
1. Supervisor Training
2. Women’s Leadership
3. Leadership Meet-Ups
4. MBA Program
Staff Development
1. Continuing Education Fund
2. Book Club
3. Pelmaroq University
4. Mentorship
5. Learning Libraries
6. Department Wide Training Events

2) Poster 2:
a. Header: Perform at Highest Capacity
b. Sub-title: Be Your Best Self
c. Description: We are committed to providing programs that bring focus to your health and overall personal wellness to encourage a well balanced life
i. Healthy Living
1. Health and wellness seminars
2. Nutrition: Fruit Delivery
ii. Fitness:
1. Step Challenge
2. Virtual 5k
3. Recess
4. Golf Lessons
5. Ping Pong Club
iii. Creativity:
1. Painting
2. Photography Club
3. Virtual Trivia
iv. Mental Health:
1. Massage Therapy
2. EAP Education
v. Financial
1. 401(k)
2. Retirement education/financial planning seminars
3. Global Insurance Program education

3) Poster 3:
a. Header: Passionate Urgent and Driven to Success
b. Sub-Header: Innovation and Strategy
c. Description: We are committed to helping you connect the dots both in the industry and with our internal goals , mission, and vision.
i. Quarterly All-Hands
ii. Lumiverse
1. Internally: Departmental and Product Updates
2. Externally: Industry Knowledge
3. Culturally: Peer to Peer Community

4) Poster 4:
a. Header: Succeed as a Team
b. Sub-Header: Cultivating Collaboration
c. Description: We are committed to creating a culture of appreciation, teamwork, and supporting an open communication. All feedback and ideas are welcome here!
i. Team Building Events
1. Employee Focused
a. Summer Picnic
b. Employee Appreciation
c. Diwali
d. Holiday Party
e. Department Appreciation
2. Family Friendly
a. Halloween
b. Bring your Kids to Work Day
3. Awards
a. Peer to Peer: QuickNod Awards
b. Leadership: Crest of Merit
4. Surveys
a. New Hire
b. Employee Engagement
Updates

Target Market(s)

Internal Employees

Industry/Entity Type

Healthcare

Font styles to use
Sans Serif

Requirements
Must have
• Job Type: Posters
• Task Outline: Create Vector Art for 4 icons and 4 posters
• Fonts and Styles to Use: SourceSansPro
Nice to have
• There is an attachment with suggested concepts and styles that we like.
Should not have
• The poster should not be very wordy or hard to read in passing.

```html
<!DOCTYPE html>
<html lang="en">
<head>
<meta charset="utf-8">
<title>Succeed as a Team – Pelmaroq</title>
<link rel="stylesheet" href="https://fonts.googleapis.com/css2?family=Source+Sans+3:ital,wght@0,300;0,400;0,600;0,700;1,300&display=swap">
<style>
  :root {
    --orange: #f29f38;
    --orange-deep: #d4892d;
    --orange-soft: #fbe3c4;
    --white: #ffffff;
    --navy: #1e2a56;
    --brand-red: #e8562a;
    --frame: #222222;
  }
  * { margin: 0; padding: 0; box-sizing: border-box; }
  html, body {
    width: 789px; height: 1200px; overflow: hidden;
    background: var(--white);
    font-family: "Source Sans 3", "Source Sans Pro", sans-serif;
  }
  .canvas { position: relative; width: 789px; height: 1200px; }
  .backdrop { position: absolute; inset: 0; width: 789px; height: 1200px; }
  .headline {
    position: absolute; left: 158px; top: 72px;
    color: var(--orange); font-weight: 700; font-size: 59px; line-height: 55px;
  }
  .subtitle {
    position: absolute; left: 159px; top: 190px;
    color: var(--orange); font-weight: 300; font-style: italic; font-size: 38px; line-height: 39px;
  }
  .intro {
    position: absolute; left: 169px; top: 399px; width: 215px;
    color: var(--white); font-weight: 600; font-size: 23px; line-height: 28.6px;
  }
  .events { position: absolute; left: 388px; top: 427px; width: 277px; color: var(--white); }
  .events-title {
    padding-left: 7px; font-weight: 600; font-size: 24px; line-height: 28px; margin-bottom: 14px;
  }
  .event-group { padding: 5px 0 8px 7px; }
  .event-group.is-shaded { background: var(--orange-deep); }
  .event-group h3 { font-weight: 600; font-size: 25px; line-height: 25px; }
  .event-group ul { list-style: none; }
  .event-group li {
    font-weight: 300; font-size: 15.3px; line-height: 18.2px; padding-left: 15px; position: relative;
  }
  .event-group li::before { content: "•"; position: absolute; left: 0; }
  .campaign-panel {
    position: absolute; left: 440px; top: 980px; width: 168px; height: 168px;
    border-radius: 12px;
    background: linear-gradient(135deg, var(--orange-soft), var(--orange));
  }
  .brand {
    position: absolute; left: 162px; top: 1089px;
    display: flex; align-items: center; gap: 14px;
  }
  .brand-square { width: 40px; height: 40px; background: var(--brand-red); }
  .brand-name { color: var(--navy); font-weight: 700; font-size: 38px; line-height: 40px; }
</style>
</head>
<body>
<div class="canvas">
  <svg class="backdrop" viewBox="0 0 827 1258" aria-hidden="true">
    <path class="wave" fill="#f29f38"
      d="M128,395 C330,320 600,330 697,252 L697,935 C600,975 450,1000 330,1012 L128,1012 Z"/>
    <rect class="frame" x="128.5" y="15.5" width="569" height="1230" fill="none" stroke="#222" stroke-width="1"/>
  </svg>

  <h1 class="headline">Succeed as<br>a Team</h1>
  <p class="subtitle">Cultivating<br>Collaboration</p>

  <p class="intro">We are committed<br>to creating<br>a culture of<br>appreciation,<br>teamwork,<br>and supporting<br>an open<br>communication.<br>All feedback<br>and ideas are<br>welcome here!</p>

  <section class="events">
    <h2 class="events-title">TEAM BUILDING<br>EVENTS</h2>
    <div class="event-group is-shaded">
      <h3>Employee Focused</h3>
      <ul>
        <li>Summer Picnic</li>
        <li>Employee Appreciation</li>
        <li>Diwali</li>
        <li>Holiday Party</li>
        <li>Department Appreciation</li>
      </ul>
    </div>
    <div class="event-group">
      <h3>Family Friendly</h3>
      <ul>
        <li>Halloween</li>
        <li>Bring your Kids to Work Day</li>
      </ul>
    </div>
    <div class="event-group is-shaded">
      <h3>Awards</h3>
      <ul>
        <li>Peer to Peer: QuickNod Awards</li>
        <li>Leadership: Crest of Merit</li>
      </ul>
    </div>
    <div class="event-group">
      <h3>Surveys</h3>
      <ul>
        <li>New Hire</li>
        <li>Employee Engagement</li>
      </ul>
    </div>
  </section>

  <div class="campaign-panel" role="img" aria-label="Area for the four campaign icons"></div>

  <div class="brand">
    <span class="brand-square"></span>
    <span class="brand-name">Pelmaroq</span>
  </div>
</div>
</body>
</html>
```